Business card design for a engineering company

I need a double sided business card design for my company "Velbrook Stream Systems". The card will be used in Malaysia. Sleek and professional, with a little design flare to it.
Information to showcase:
1. Company logo
2. Name, title, phone, email address, website address
3. our products "Pumping technology, Valve & actuation, Air Moving Technology
Example:
Mark Dovan
Business manager
mark.dovan@velbrook-example.com
www.velbrook-example.com.my
- Pumping technology
- Valve & actuation
- Air moving technology
Target Market(s)
engineers, purchasing managers
Industry/Entity Type
Business
Contact Information for Business Card
Mark Dovan
Business manager
mark.dovan@velbrook-example.com
www.velbrook-example.com.my
- Pumping technology
- Valve & actuation
- Air moving technology
catch phrase : "Solving flow challenges, exceeding expectations"

```html
<!DOCTYPE html>
<html lang="en">
<head>
<meta charset="utf-8">
<title>Velbrook Stream Systems – Business Card</title>
<link rel="stylesheet" href="https://fonts.googleapis.com/css2?family=Arimo:wght@400;700&display=swap">
<style>
  :root {
    --backdrop: #9b9b9b;
    --paper: #f7f7f6;
    --orange-light: #f4b552;
    --orange: #eea236;
    --orange-deep: #e58a2c;
    --navy: #173f52;
    --teal: #2c6478;
    --grey-text: #8d9296;
    --white: #ffffff;
  }
  * { box-sizing: border-box; margin: 0; padding: 0; }
  html, body { width: 1200px; height: 1200px; overflow: hidden; }
  body {
    background: var(--backdrop);
    font-family: "Arimo", Arial, sans-serif;
    position: relative;
  }
  .card {
    position: absolute;
    left: 180px;
    width: 840px;
    height: 480px;
    background: var(--paper);
    box-shadow: 0 14px 30px rgba(0,0,0,0.25);
    overflow: hidden;
  }
  .card--front { top: 90px; display: flex; }
  .card--back { top: 630px; }

  /* Front */
  .contact-panel {
    width: 380px;
    height: 100%;
    background: radial-gradient(circle at 60% 30%, var(--orange-light), var(--orange) 55%, var(--orange-deep));
    padding: 70px 0 0 48px;
    position: relative;
  }
  .divider {
    width: 9px;
    height: 100%;
    background: var(--navy);
  }
  .brand-panel {
    flex: 1;
    display: flex;
    align-items: center;
    justify-content: center;
  }
  .person-name {
    font-weight: 700;
    font-size: 30px;
    color: var(--navy);
    line-height: 1.1;
  }
  .person-title {
    font-size: 22px;
    color: var(--white);
    margin-top: 4px;
  }
  .contact-list {
    position: absolute;
    left: 48px;
    bottom: 56px;
    list-style: none;
  }
  .contact-list li {
    display: flex;
    align-items: center;
    gap: 14px;
    font-size: 17px;
    color: var(--navy);
    height: 32px;
  }
  .contact-icon { width: 22px; height: 22px; flex: none; }

  .brand {
    display: flex;
    align-items: center;
    gap: 14px;
  }
  .brand-mark {
    width: 30px; height: 30px;
    border-radius: 50%;
    background: var(--teal);
  }
  .brand-name {
    font-weight: 700;
    font-size: 30px;
    color: var(--teal);
    letter-spacing: 0.5px;
  }

  /* Back */
  .card--back .brand { position: absolute; left: 0; right: 0; top: 150px; justify-content: center; }
  .product-list {
    position: absolute;
    left: 0; right: 0; top: 250px;
    list-style: none;
    text-align: center;
    color: var(--grey-text);
    font-size: 19px;
    line-height: 34px;
  }
</style>
</head>
<body>
  <section class="card card--front">
    <div class="contact-panel">
      <h1 class="person-name">Mark Dovan</h1>
      <p class="person-title">Business manager</p>
      <ul class="contact-list">
        <li>
          <svg class="contact-icon" viewBox="0 0 22 22" aria-hidden="true"><rect width="22" height="22" rx="3" fill="#173f52"/><path d="M7 5c1 0 2 2.5 2 3s-1 1-1 1.5 2.5 3.5 3.5 3.5 1-1 1.5-1 3 1 3 2-1.5 2-2.5 2C9 16 5 11 5 8c0-1 1-3 2-3z" fill="#fff"/></svg>
          (+6) 07 418 2905
        </li>
        <li>
          <svg class="contact-icon" viewBox="0 0 22 22" aria-hidden="true"><rect width="22" height="22" rx="3" fill="#173f52"/><rect x="5" y="9" width="12" height="8" fill="#fff"/><rect x="7" y="5" width="8" height="4" fill="#fff"/><rect x="7" y="12" width="8" height="1.5" fill="#173f52"/></svg>
          (+6) 07 418 2916
        </li>
        <li>
          <svg class="contact-icon" viewBox="0 0 22 22" aria-hidden="true"><rect width="22" height="22" rx="3" fill="#173f52"/><rect x="4.5" y="6.5" width="13" height="9" fill="none" stroke="#fff" stroke-width="1.5"/><path d="M4.5 6.5 11 12l6.5-5.5" fill="none" stroke="#fff" stroke-width="1.5"/></svg>
          mark.dovan@velbrook-example.com
        </li>
        <li>
          <svg class="contact-icon" viewBox="0 0 22 22" aria-hidden="true"><rect width="22" height="22" rx="3" fill="#173f52"/><circle cx="11" cy="11" r="6" fill="none" stroke="#fff" stroke-width="1.5"/><path d="M5 11h12M11 5c-3 3-3 9 0 12M11 5c3 3 3 9 0 12" fill="none" stroke="#fff" stroke-width="1.2"/></svg>
          www.velbrook-example.com.my
        </li>
      </ul>
    </div>
    <div class="divider"></div>
    <div class="brand-panel">
      <div class="brand">
        <span class="brand-mark"></span>
        <span class="brand-name">Velbrook Stream Systems</span>
      </div>
    </div>
  </section>

  <section class="card card--back">
    <div class="brand">
      <span class="brand-mark"></span>
      <span class="brand-name">Velbrook Stream Systems</span>
    </div>
    <ul class="product-list">
      <li>Pumping technology</li>
      <li>Valve &amp; actuation</li>
      <li>Air moving technology</li>
    </ul>
  </section>
</body>
</html>
```